Webdesign Tischlerei Wendholt GmbH
Zielgruppe
Tischlerei - Meisterbetrieb -> Zielgruppe Privatkunden + gewerbliche Kunden
Aufgabenstellung
KEINE Kopie der alten Seite, da sich das gesamte Erscheinungsbild wesentlich moderner gestaltet... aufbauend auf dem neuen Unternehmenslogo. Es soll mit den vorhandenen Farben aus dem Logo gearbeitet werden - jedoch nicht verspielt sein.
ACHTUNG: bei den beiden mitgelieferten Dateien, welche dir Icons als Abbildung haben, ist nicht korrekte Logo verbaut, sofern diese Icons nicht verwendbar sind, bitte passende Logos für die einzelnen Kategoerien Wählen.

```html
<!DOCTYPE html>
<html lang="de">
<head>
<meta charset="utf-8">
<title>Tischlerei Wendholt GmbH</title>
<link rel="stylesheet" href="https://fonts.googleapis.com/css2?family=Lato:ital,wght@0,400;0,700;1,400&family=Noto+Serif:wght@400;700&display=swap">
<style>
:root{
  --canvas:#ebecee;
  --forest:#15251f;
  --forest-line:#1d2f29;
  --wood:#b97a35;
  --gold-line:#7d6238;
  --paper:#ffffff;
  --mist:#f7f8f8;
  --ink:#1f2523;
  --white:#ffffff;
}
*{margin:0;padding:0;box-sizing:border-box}
html,body{width:1200px;height:2400px;overflow:hidden;background:var(--canvas)}
body{position:relative;font-family:"Lato",sans-serif;color:var(--ink)}
.abs{position:absolute}

.site{position:absolute;left:166px;top:114px;width:868px;height:2171px;background:var(--paper)}

/* hero */
.hero{position:absolute;left:166px;top:114px;width:868px;height:452px;background:var(--forest);color:var(--white)}
.nav-brand{position:absolute;left:239px;top:136px;display:flex;align-items:center;gap:5px;font-family:"Noto Serif",serif;font-size:6.5px;line-height:8px;color:var(--white);white-space:nowrap}
.nav-brand .mark{width:14px;height:14px;border:1px solid var(--white);flex:none}
.nav-link{position:absolute;top:140px;font-size:8.5px;color:var(--white)}
.hero-brand{position:absolute;left:491px;top:204px;display:flex;align-items:center;gap:12px;font-family:"Noto Serif",serif;font-size:19px;color:var(--white)}
.hero-brand .mark{width:28px;height:28px;border:2px solid var(--white)}
.tag{position:absolute;height:25px;border:1px solid var(--gold-line);font-family:"Noto Serif",serif;font-weight:700;font-size:8.5px;color:var(--white);display:flex;align-items:center;justify-content:center;width:85px}
.hero-title{position:absolute;left:166px;width:868px;top:316px;text-align:center;font-family:"Noto Serif",serif;font-weight:700;font-size:31px;line-height:34px}
.hero-lead{position:absolute;left:166px;width:868px;top:393px;text-align:center;font-size:14.5px;line-height:19px}
.btn{position:absolute;height:31px;border-radius:4px;font-size:9.5px;display:flex;align-items:center;justify-content:center}
.btn-wood{background:var(--wood);color:var(--white)}
.btn-line{border:1px solid var(--white);color:var(--white)}

/* services */
.section-title{position:absolute;left:166px;width:868px;text-align:center;font-family:"Noto Serif",serif;font-weight:700;font-size:15.5px}
.grid{position:absolute;left:239px;top:667px;width:723px;height:503px;background:var(--forest);display:grid;grid-template-columns:repeat(4,1fr);grid-template-rows:repeat(3,1fr)}
.cell{position:relative;padding:20px 10px 0 11px;color:var(--white);border-right:1px solid var(--forest-line);border-bottom:1px solid var(--forest-line)}
.cell .num{font-family:"Noto Serif",serif;font-size:6.5px;padding-bottom:4px;width:52px;border-bottom:1px solid var(--gold-line)}
.cell h3{font-weight:400;font-size:12px;line-height:14.5px;margin-top:25px;text-transform:uppercase}
.cell p{font-size:8.4px;line-height:11px;margin-top:7px}
.cell.accent{background:var(--wood);padding:16px 12px 0 22px}
.cell.accent li{list-style:none;font-size:8.4px;line-height:11px;margin-bottom:7px}

/* cta */
.band{position:absolute;left:166px;width:868px;background:var(--mist)}
.cta-text{position:absolute;left:166px;width:868px;top:1257px;text-align:center;font-size:12.5px;line-height:16.5px}

/* about */
.photo{position:absolute}
.about-title{position:absolute;left:239px;top:1417px;font-family:"Noto Serif",serif;font-weight:700;font-size:15.5px}
.about-text{position:absolute;font-size:11.5px;line-height:14.5px}

/* contact */
.contact{position:absolute;left:239px;top:1966px;font-size:12.5px;line-height:16px}
.contact p{margin-bottom:9px}

/* footer */
.footer{position:absolute;left:166px;top:2211px;width:868px;height:74px;background:var(--forest);color:var(--white)}
.foot-link{position:absolute;top:2245px;font-size:8px;color:var(--white)}
</style>
</head>
<body>
<div class="site"></div>

<header class="hero"></header>
<div class="nav-brand"><span class="mark"></span><span>Tischlerei Wendholt<br>GmbH</span></div>
<span class="nav-link" style="left:342px">Start</span>
<span class="nav-link" style="left:415px">Über uns</span>
<span class="nav-link" style="left:491px">Leistungen</span>
<span class="nav-link" style="left:720px">f.wendholt@tischlerei-wendholt.de</span>
<span class="nav-link" style="left:893px">(0 37 22) 4 18 63</span>

<div class="hero-brand"><span class="mark"></span>Tischlerei Wendholt GmbH</div>

<svg class="abs" style="left:0;top:0" width="1200" height="600" aria-hidden="true">
  <g stroke="#7d6238" stroke-width="1" fill="none">
    <path d="M347 241H424"/>
    <path d="M323 362H347V270H407"/>
    <path d="M347 460H363V310H391"/>
    <path d="M776 241H852"/>
    <path d="M876 362H852V270H792"/>
    <path d="M854 460H837V310H809"/>
  </g>
</svg>
<div class="tag" style="left:261px;top:209px">Montage</div>
<div class="tag" style="left:239px;top:313px">Fertigung</div>
<div class="tag" style="left:261px;top:398px">Beratung</div>
<div class="tag" style="left:852px;top:210px">Planung</div>
<div class="tag" style="left:876px;top:313px">Maßarbeit</div>
<div class="tag" style="left:854px;top:400px">Materialauswahl</div>

<h1 class="hero-title" style="color:var(--white)">Maßarbeit aus Holz.<br>Mit Erfahrung seit 1928.</h1>
<p class="hero-lead" style="color:var(--white)">Wir planen, fertigen und montieren individuelle Tischlerarbeiten –<br>präzise und passend zu Ihren Anforderungen.</p>
<a class="btn btn-wood" style="left:484px;top:464px;width:109px">Leistungen ansehen</a>
<a class="btn btn-line" style="left:607px;top:464px;width:109px">Kontakt aufnehmen</a>

<h2 class="section-title" style="top:617px">Was wir machen</h2>
<section class="grid">
  <div class="cell"><div class="num">01</div><h3>Wohnraummöbel</h3><p>Maßgefertigte Möbel für Wohnräume – passend zu Raum, Stil und täglicher Nutzung.</p></div>
  <div class="cell accent"><ul>
    <li>Individuelle Küchen</li>
    <li>Individuelle Badmöbel</li>
    <li>Original Rotholm-Küchen aus Sachsen</li>
    <li>Aus Alt mach Neu – Küchenfronten- und Arbeitsplattenwechsel</li>
    <li>Arbeitsplatten aus Naturstein</li>
    <li>Nischenrückwände mit Bild / Lacklerung / Digitaldruck</li>
  </ul></div>
  <div class="cell"><div class="num">03</div><h3>Innenausbau (Wand, Decke, Boden)</h3><p>Durchdachte Lösungen für Wand, Decke und Boden – funktional, sauber und hochwertig umgesetzt.</p></div>
  <div class="cell"><div class="num">04</div><h3>Fenster und Türen</h3><p>Passgenaue Fenster und Türen aus Holz – für Sicherheit, Komfort und ein stimmiges Gesamtbild.</p></div>
  <div class="cell"><div class="num">05</div><h3>Praxiseinrichtungen / Ladenbau</h3><p>Einrichtungen für Praxen, Verkaufsräume und gewerbliche Bereiche – individuell geplant und gefertigt.</p></div>
  <div class="cell"><div class="num">06</div><h3>Museumsarchitektur</h3><p>Maßgeschneiderte Lösungen für Ausstellungen, Museen und besondere Räume mit hohen Anforderungen.</p></div>
  <div class="cell"><div class="num">07</div><h3>CNC-Kleinserien</h3><p>Präzise CNC-Fertigung für kleine Serien, Sonderteile und wiederkehrende Bauteile.</p></div>
  <div class="cell"><div class="num">08</div><h3>Glaserei im Haus</h3><p>Glaslösungen aus eigener Bearbeitung – klar, passgenau und abgestimmt auf Ihr Projekt.</p></div>
  <div class="cell"><div class="num">09</div><h3>Treppen</h3><p>Individuelle Treppenlösungen aus Holz – stabil, funktional und passend zum Raum gestaltet.</p></div>
  <div class="cell"><div class="num">10</div><h3>Restauration</h3><p>Fachgerechte Aufarbeitung und Erhaltung historischer Möbel, Bauteile und besonderer Stücke.</p></div>
  <div class="cell"><div class="num">11</div><h3>Orgelgehäuse</h3><p>Gehäuse und Bauteile für den Orgelbau – gefertigt mit Präzision und handwerklicher Erfahrung.</p></div>
  <div class="cell"><div class="num">12</div><h3>Serviceleistungen</h3><p>Reparatur, Wartung und Beratung – zuverlässig auch nach Fertigung und Montage für Sie da.</p></div>
</section>

<div class="band" style="top:1202px;height:165px"></div>
<h2 class="section-title" style="top:1226px">Sie planen ein individuelles Projekt?</h2>
<p class="cta-text">Ob Möbel, Küche, Innenausbau oder Sonderanfertigung – wir beraten Sie persönlich und<br>finden die passende Lösung.</p>
<a class="btn btn-wood" style="left:542px;top:1304px;width:117px;height:37px">Kontakt aufnehmen</a>

<div class="photo" role="img" aria-label="Foto: Einbauschrank aus Eichenholz mit offenen Regalfächern" style="left:607px;top:1370px;width:355px;height:235px;background:linear-gradient(90deg,#b07a4c 0%,#c99062 40%,#a8703f 75%,#2d2a28 100%)"></div>
<h2 class="about-title">Wer wir sind</h2>
<p class="about-text" style="left:239px;top:1447px;width:330px">Seit Generationen verbindet die Tischlerei Wendholt traditionelles Handwerk mit moderner Fertigung.<br>Wir entwickeln Lösungen aus Holz, die funktional, langlebig und auf Ihre Räume abgestimmt sind.<br>Von der Beratung über die Produktion bis zur Montage begleiten wir jedes Projekt persönlich und zuverlässig.</p>

<div class="photo" role="img" aria-label="Foto: Freitragende Holztreppe mit weißem Sessel davor" style="left:239px;top:1613px;width:354px;height:235px;background:linear-gradient(160deg,#9a9792 0%,#7f7a72 45%,#6a5440 75%,#5a4836 100%)"></div>
<p class="about-text" style="left:631px;top:1681px;width:310px">Ob Wohnmöbel, Küche, Innenausbau oder Sonderanfertigung – jedes Projekt beginnt mit einer persönlichen Beratung und einem genauen Blick auf Ihre Anforderungen.<br>So entstehen Lösungen, die nicht nur gut aussehen, sondern im Alltag dauerhaft überzeugen.<br><br><i>Planung, Produktion und Montage aus einer Hand.</i></p>

<div class="band" style="top:1848px;height:363px"></div>
<div class="contact">
  <p>Tischlerei Wendholt GmbH<br>Lindenweg 7<br>09876 Holzhausen</p>
  <p style="margin-top:20px">(0 37 22) 4 18 63</p>
  <p>f.wendholt@tischlerei-wendholt.de</p>
  <p>Anfahrt / Karte ansehen</p>
</div>
<div class="photo" role="img" aria-label="Karte mit dem Standort der Tischlerei" style="left:629px;top:1905px;width:270px;height:256px;background:linear-gradient(135deg,#eef0f3 0%,#e3e7ee 60%,#dde3ec 100%)"></div>

<footer class="footer"></footer>
<div class="nav-brand" style="top:2240px"><span class="mark"></span><span>Tischlerei Wendholt<br>GmbH</span></div>
<span class="foot-link" style="left:347px">Impressum</span>
<span class="foot-link" style="left:418px">Datenschutz</span>
<span class="foot-link" style="left:502px">Erklärung zur Barrierefreiheit</span>
<span class="foot-link" style="left:798px">© Tischlerei Wendholt GmbH</span>
</body>
</html>
```